Business Journal Ad for a Commercial Real Estate Firm

I need to have an ad designed to be included in a business journal with a very short timeline (due 5/14/21). I can include the copies they came up with which I'm not a fan of. The ad size should be either: 4.875 x 6.125 OR 2.345 x 6.125. The content should include information on all three divisions of the company as shown in one of the example ads that are attached with the same contact information and company logos that are attached. You can view our company website at www.dalbyfenwickre.com for additional information, photos, sample marketing, etc.

Target Market(s)

Business owners, creative, property owners, 35+

Industry/Entity Type

Real Estate

Requirements
Must have
• Graphics, color, green, company logo, contact info

```html
<!DOCTYPE html>
<html lang="en">
<head>
<meta charset="utf-8">
<title>Dalby-Fenwick Real Estate – Journal Ad</title>
<link rel="stylesheet" href="https://fonts.googleapis.com/css2?family=Sorts+Mill+Goudy&family=Crimson+Pro:wght@700&family=Montserrat:wght@400;500;700&display=swap">
<style>
  :root {
    --brand-green: #0a663c;
    --ink: #2a2a2a;
    --paper: #ffffff;
    --sky: #8fb6e6;
    --facade: #a9a49c;
  }
  html, body { margin: 0; padding: 0; overflow: hidden; }
  body { width: 973px; height: 1200px; background: var(--paper); }
  .ad {
    position: relative;
    width: 973px; height: 1200px;
    overflow: hidden;
    background: var(--paper);
    font-family: "Montserrat", sans-serif;
    color: var(--ink);
  }
  .ad-shapes { position: absolute; inset: 0; }
  .brand { position: absolute; left: 0; top: 0; width: 973px; }
  .brand-dot {
    position: absolute; left: 60px; top: 70px;
    width: 160px; height: 160px; border-radius: 50%;
    background: var(--paper);
  }
  .brand-name {
    position: absolute; left: 248px; top: 48px;
    margin: 0;
    font-family: "Sorts Mill Goudy", serif;
    font-weight: 400;
    color: var(--paper);
    font-size: 104px; line-height: 1;
    letter-spacing: -1px;
    white-space: nowrap;
  }
  .brand-tag {
    position: absolute; left: 324px; top: 170px;
    font-family: "Sorts Mill Goudy", serif;
    font-weight: 400;
    color: var(--paper);
    font-size: 44px; line-height: 1;
    letter-spacing: 11px;
    white-space: nowrap;
  }
  .headline {
    position: absolute; left: 0; top: 352px; width: 973px;
    margin: 0; text-align: center;
    font-family: "Crimson Pro", serif; font-weight: 700;
    font-size: 45px; line-height: 60px;
    color: var(--ink);
  }
  .headline .accent { color: var(--brand-green); }
  .services { position: absolute; left: 85px; top: 570px; width: 360px; color: var(--paper); }
  .service { margin: 0 0 22px; }
  .service-title {
    margin: 0; padding: 0 0 6px 32px;
    font-weight: 700; font-size: 24px; line-height: 30px;
    border-bottom: 2px solid var(--paper);
  }
  .contact-row {
    display: flex; align-items: center; gap: 10px;
    margin: 6px 0 0; font-size: 25px; line-height: 30px; font-weight: 500;
    white-space: nowrap;
  }
  .contact-row svg { width: 22px; height: 22px; flex: none; }
  .photo { position: absolute; left: 0; top: 0; }
  .office { position: absolute; left: 83px; top: 1062px; }
  .office-label {
    margin: 0 0 6px 30px; font-weight: 700; font-size: 24px;
    letter-spacing: 0.5px; color: var(--brand-green);
  }
  .office-address {
    display: flex; gap: 10px; font-style: normal;
    font-size: 23.5px; line-height: 31px; font-weight: 500; color: var(--ink);
  }
  .office-address svg { width: 20px; height: 30px; flex: none; margin-top: 0; }
  .site {
    position: absolute; left: 566px; top: 1128px;
    display: flex; align-items: center; gap: 10px;
    font-size: 25px; font-weight: 500; color: var(--ink);
  }
  .site svg { width: 22px; height: 22px; }
  .site strong { color: var(--brand-green); font-weight: 700; }
</style>
</head>
<body>
<main class="ad">
  <svg class="ad-shapes" width="973" height="1200" viewBox="0 0 973 1200" aria-hidden="true">
    <path fill="var(--brand-green)" d="M0,0 H973 V252 C760,262 520,322 350,326 C220,330 90,312 0,285 Z"/>
    <path fill="var(--brand-green)" d="M0,559 C120,522 290,488 420,535 C460,550 490,566 505,581 L600,960 L805,979 C860,1040 900,1068 958,1082 C700,1072 430,1004 241,1014 C140,1020 60,1038 0,1053 Z"/>
    <circle cx="686" cy="768" r="254" fill="var(--brand-green)"/>
  </svg>

  <svg class="photo" width="973" height="1200" viewBox="0 0 973 1200" role="img" aria-label="Photo of a retail strip centre storefront under a clear blue sky">
    <defs>
      <linearGradient id="storefront" x1="0" y1="0" x2="0" y2="1">
        <stop offset="0" stop-color="var(--sky)"/>
        <stop offset="0.35" stop-color="#b9b7b0"/>
        <stop offset="0.7" stop-color="var(--facade)"/>
        <stop offset="1" stop-color="#d8d4cc"/>
      </linearGradient>
    </defs>
    <circle cx="674" cy="770" r="230" fill="url(#storefront)" stroke="var(--paper)" stroke-width="3"/>
  </svg>

  <header class="brand">
    <span class="brand-dot"></span>
    <h1 class="brand-name">Dalby-Fenwick</h1>
    <div class="brand-tag">REAL ESTATE</div>
  </header>

  <h2 class="headline">Impacting Fayetteville and<br><span class="accent">Surrounding areas for over 10 years.</span></h2>

  <section class="services">
    <div class="service">
      <h3 class="service-title">Commercial Sales</h3>
      <p class="contact-row"><svg viewBox="0 0 24 24"><circle cx="12" cy="12" r="10.5" fill="none" stroke="#fff" stroke-width="1.6"/><path d="M8.5 7.5l2 2-1 1.3c.8 1.6 1.9 2.7 3.5 3.5l1.3-1 2 2-1.3 1.4c-3.6-.5-7-3.9-7.5-7.5z" fill="none" stroke="#fff" stroke-width="1.4" stroke-linejoin="round"/></svg>910.555.0143</p>
      <p class="contact-row"><svg viewBox="0 0 24 24" fill="none" stroke="#fff" stroke-width="1.6"><circle cx="12" cy="12" r="10"/><ellipse cx="12" cy="12" rx="4.5" ry="10"/><path d="M2 12h20M4 6.5h16M4 17.5h16"/></svg>DalbyFenwickRE.com</p>
    </div>
    <div class="service">
      <h3 class="service-title">Commercial<br>Property Managment</h3>
      <p class="contact-row"><svg viewBox="0 0 24 24"><circle cx="12" cy="12" r="10.5" fill="none" stroke="#fff" stroke-width="1.6"/><path d="M8.5 7.5l2 2-1 1.3c.8 1.6 1.9 2.7 3.5 3.5l1.3-1 2 2-1.3 1.4c-3.6-.5-7-3.9-7.5-7.5z" fill="none" stroke="#fff" stroke-width="1.4" stroke-linejoin="round"/></svg>910.555.0178</p>
      <p class="contact-row"><svg viewBox="0 0 24 24" fill="none" stroke="#fff" stroke-width="1.6"><circle cx="12" cy="12" r="10"/><ellipse cx="12" cy="12" rx="4.5" ry="10"/><path d="M2 12h20M4 6.5h16M4 17.5h16"/></svg>DalbyFenwickPM.com</p>
    </div>
    <div class="service">
      <h3 class="service-title">Residential Homes</h3>
      <p class="contact-row"><svg viewBox="0 0 24 24"><circle cx="12" cy="12" r="10.5" fill="none" stroke="#fff" stroke-width="1.6"/><path d="M8.5 7.5l2 2-1 1.3c.8 1.6 1.9 2.7 3.5 3.5l1.3-1 2 2-1.3 1.4c-3.6-.5-7-3.9-7.5-7.5z" fill="none" stroke="#fff" stroke-width="1.4" stroke-linejoin="round"/></svg>910.555.0126</p>
      <p class="contact-row"><svg viewBox="0 0 24 24" fill="none" stroke="#fff" stroke-width="1.6"><circle cx="12" cy="12" r="10"/><ellipse cx="12" cy="12" rx="4.5" ry="10"/><path d="M2 12h20M4 6.5h16M4 17.5h16"/></svg>DalbyFenwickHomes.com</p>
    </div>
  </section>

  <footer>
    <div class="office">
      <p class="office-label">OFFICE LOCATION:</p>
      <address class="office-address">
        <svg viewBox="0 0 20 30" fill="none" stroke="var(--brand-green)" stroke-width="2"><path d="M10 2a6 6 0 0 1 6 6c0 4.5-6 12-6 12S4 12.5 4 8a6 6 0 0 1 6-6z"/><circle cx="10" cy="8" r="2.2"/><path d="M3 24c0 2 14 2 14 0"/></svg>
        <span>418 W. Linden Hollow Rd.,<br>Fayetteville, Nc 28303</span>
      </address>
    </div>
    <div class="site">
      <svg viewBox="0 0 24 24" fill="none" stroke="var(--brand-green)" stroke-width="1.6"><circle cx="12" cy="12" r="10"/><ellipse cx="12" cy="12" rx="4.5" ry="10"/><path d="M2 12h20M4 6.5h16M4 17.5h16"/></svg>
      <span>www.<strong>dalbyfenwickre</strong>.com</span>
    </div>
  </footer>
</main>
</body>
</html>
```